Home & Landing Page REDESIGN needed for Psychology Group

We need a redesign for the template home and landing pages for our psychology group.

Ideally we want a similar layout in the core features, but we want a newer, fresher and more professional design overall.

Our developer will implement the changes from the winning design.

Logo to stay the same.

Please ensure you stay within the same color scheme as the LOGOs 3 main colors.

We want to convey professional, modern, friendly and caring.

Here is the main page template:

http://www.lowrenclinic.com.au/psychologist-melbourne/

and

http://www.lowrenclinic.com.au

*note: we are creating an intro video, please ensure it is included in your brief, near the top of the site* - it is not included on the current site yet but we need it included in all designs.

Target Market(s)

people suffering anxiety, depression or stress that need a psychologist

Industry/Entity Type

Psychology

Number of Pages Required

2 page

Font styles to use
Sans Serif

Colors
86cfc6
85cae6
b7a5cd

Requirements
Must have
• search bar functionality in the top fold of the page, strong focus that we are experienced in anxiety, depression and stress counselling.
• Lots of images and pictures.
• **MUST HAVE: the search square area as it is, unfortunately this cannot be a bar due to development issues with the theme. Please make sure all designs have the search function like it is showing (in a square/rectangle)**
• Must also keep:
• - content area for both home page and city landing pages
• - banner area with search bar same style
• - an area for faqs and blog
• - locations across Australia
• We want most of the same areas, just a refresh so they look better and more polished and professional.
• We are also having an intro video designed, so please include that in your design. (its not in our current web design, but needs to be in the new design)
Should not have
• No orange type colors

```html
<!DOCTYPE html>
<html lang="en">
<head>
<meta charset="utf-8">
<title>Calmbridge Psychology – Anxiety, Depression &amp; Stress Psychologists</title>
<link href="https://fonts.googleapis.com/css2?family=Lato:wght@300;400;700&display=swap" rel="stylesheet">
<style>
:root{
  --teal:#86cfc6;
  --teal-btn:#6fc3b5;
  --blue:#85cae6;
  --blue-btn:#6dbde0;
  --purple:#b7a5cd;
  --purple-deep:#a48fc4;
  --ink:#4a4a4a;
  --muted:#8e8e8e;
  --line:#e4e4e4;
  --soft:#f6f6f6;
  --white:#fff;
}
*{margin:0;padding:0;box-sizing:border-box}
html,body{width:1200px;height:3888px;overflow:hidden}
body{position:relative;font-family:'Lato',sans-serif;color:var(--ink);background:var(--white)}
.abs{position:absolute}
.btn{position:absolute;display:flex;align-items:center;justify-content:center;color:#fff;font-size:11px;letter-spacing:.5px;text-transform:uppercase;border-radius:2px}
.btn.teal{background:var(--teal-btn)}
.btn.blue{background:var(--blue-btn)}
.btn.purple{background:var(--purple-deep)}
.section-title{position:absolute;left:0;width:1200px;text-align:center;font-weight:300;font-size:28px;letter-spacing:2px;color:#555}

/* top bar + nav */
.topbar{left:0;top:0;width:1200px;height:26px;background:var(--purple-deep)}
.topbar ul{position:absolute;right:200px;top:7px;display:flex;list-style:none;font-size:10px;color:#fff}
.topbar li{padding:0 14px;border-left:1px solid rgba(255,255,255,.4)}
.topbar li:first-child{border-left:none}
.nav{left:0;top:26px;width:1200px;height:78px;background:#fff}
.logo{position:absolute;display:flex;align-items:center;gap:8px;font-size:19px;font-weight:700;color:var(--purple-deep)}
.logo i{display:block;width:22px;height:22px;border-radius:50%;background:var(--teal)}
.nav .logo{left:202px;top:26px}
.nav ul{position:absolute;left:405px;top:33px;display:flex;gap:30px;list-style:none;font-size:13px;color:#666}

/* hero */
.hero{left:0;top:104px;width:1200px;height:518px;background:linear-gradient(120deg,#8a8580 0%,#c9b9a8 35%,#e7dccd 55%,#9b8f86 100%)}
.hero-title{left:0;top:214px;width:1200px;text-align:center;color:#fff;font-size:21px;font-weight:300}
.dots{left:566px;top:364px;display:flex;gap:12px}
.dots span{width:8px;height:8px;border-radius:50%;background:rgba(255,255,255,.55)}
.dots span:nth-child(2){background:#fff}
.search{left:0;top:414px;width:1200px;height:104px;background:rgba(70,90,110,.55)}
.field{position:absolute;top:34px;height:36px;border:1px solid rgba(255,255,255,.6);background:rgba(255,255,255,.12);color:#fff;font-size:11px;padding:11px 10px;white-space:nowrap;overflow:hidden}
.field.select::after{content:"";position:absolute;right:10px;top:15px;border:4px solid transparent;border-top-color:#fff}
.search-go{position:absolute;left:962px;top:34px;width:36px;height:36px;background:var(--purple-deep);display:flex;align-items:center;justify-content:center}

/* provide */
.provide-col{position:absolute;width:220px;text-align:center}
.provide-icon{width:72px;height:72px;margin:0 auto;border-radius:50%}
.provide-label{margin-top:32px;font-size:18px;color:#555}
.provide-rule{width:64px;height:2px;margin:10px auto 0}
.provide-card{margin-top:14px;border:1px solid var(--line);padding:16px 10px 0;height:200px;font-size:11px;line-height:1.8;color:var(--muted)}

/* match */
.match{left:0;top:1232px;width:1200px;height:526px;background:linear-gradient(90deg,rgba(133,202,230,.92),rgba(120,190,225,.85) 50%,rgba(150,205,232,.9)),linear-gradient(90deg,#6c8aa0,#c9d6df)}
.match h2{position:absolute;left:0;top:74px;width:1200px;text-align:center;color:#fff;font-weight:300;font-size:28px;letter-spacing:2px}
.match .sub{position:absolute;left:0;top:118px;width:1200px;text-align:center;color:#fff;font-size:13px}
.match .point{position:absolute;top:236px;color:#fff;font-size:19px;line-height:1.45;font-weight:300;padding-left:28px}
.match .point::before{content:"";position:absolute;left:0;top:8px;border:6px solid transparent;border-left-color:#fff}

/* blog */
.blog-card{left:202px;top:1918px;width:796px;height:250px;background:#f7f7f7}
.blog-img{position:absolute;left:0;top:0;width:330px;height:250px;background:linear-gradient(135deg,#c9c1ae,#e9e2d2 50%,#7f9a74)}
.blog-img .ic{position:absolute;top:112px;width:30px;height:30px;border-radius:50%;background:var(--teal-btn)}
.blog-card h3{position:absolute;left:345px;top:38px;font-size:19px;font-weight:400;color:#555}
.blog-card p{position:absolute;left:345px;top:76px;width:425px;font-size:12px;line-height:1.75;color:#a8a8a8}
.share{position:absolute;right:22px;top:210px;font-size:11px;color:#777;display:flex;gap:8px;align-items:center}

/* faq */
.faq{left:0;top:2276px;width:1200px;height:524px;background:var(--soft)}
.faq-bar{left:202px;top:112px;width:796px;height:42px;background:var(--purple-deep);color:#fff;font-size:16px;padding:12px 18px}
.faq-bar .box{position:absolute;right:14px;top:14px;width:14px;height:14px;border:1px solid #fff}
.faq-item{position:absolute;left:202px;width:368px;height:44px;background:#fff;font-size:12px;padding:15px 16px;color:#555}
.faq-item::after{content:"";position:absolute;right:14px;top:16px;width:11px;height:11px;border:1px solid #bbb}
.faq-text{left:590px;top:186px;width:400px;font-size:11.5px;line-height:1.85;color:#666}

/* ready */
.ready-text{left:0;top:2958px;width:1200px;text-align:center;font-size:14px;color:#999}

/* locations */
.locations{left:0;top:3124px;width:1200px;height:492px;border-top:1px solid var(--line)}
.map{position:absolute;left:202px;top:80px;width:426px;height:370px;border-radius:4px;background:linear-gradient(100deg,#f2f4f5 0%,#e7eef1 45%,#cfe7f2 70%,var(--blue) 100%)}
.loc-title{left:674px;top:3276px;font-size:15px;font-weight:400;letter-spacing:1px;color:var(--purple-deep)}
.loc-list{left:674px;top:3330px;list-style:none;font-size:13px;color:#555;line-height:27px}
.loc-list li::before{content:"›";color:#999;margin-right:12px}

/* footer */
.footer{left:0;top:3616px;width:1200px;height:220px;border-top:1px solid var(--line)}
.footer .logo{left:202px;top:30px;font-size:17px}
.phone{position:absolute;left:202px;top:96px;display:flex;gap:8px;align-items:center;font-size:13px;color:#666}
.foot-col{position:absolute;top:36px;list-style:none;font-size:12px;line-height:21px;color:#555}
.join{position:absolute;left:795px;top:30px;width:203px;height:156px;background:var(--purple);color:#fff;padding:14px}
.join h4{font-size:13px;font-weight:400}
.join p{margin-top:10px;font-size:10px;line-height:1.6}
.copyright{left:0;top:3836px;width:1200px;height:52px;border-top:1px solid var(--line);text-align:center;font-size:11px;color:#777;padding-top:20px}
</style>
</head>
<body>

<header>
  <div class="abs topbar"><ul><li>About Us</li><li>Therapies We Use</li><li>Join Our Associate Program</li><li>Blog</li></ul></div>
  <nav class="abs nav">
    <div class="logo"><i></i>Calmbridge</div>
    <ul><li>Home</li><li>Counselling Types</li><li>Psychologist Locations</li><li>FAQs</li><li>Fees &amp; Rebates</li><li>Quizzes</li><li>Contact</li></ul>
  </nav>
</header>

<section class="abs hero" role="img" aria-label="Photo of two people holding hands in support, with intro video">
  <svg class="abs" style="left:556px;top:90px" width="88" height="88" viewBox="0 0 88 88"><circle cx="44" cy="44" r="41" fill="none" stroke="#fff" stroke-width="3"/><path d="M34 26 L64 44 L34 62 Z" fill="var(--teal)"/></svg>
  <h1 class="abs hero-title">Experienced and Caring Anxiety &amp; Depression Psychologists</h1>
  <div class="btn blue" style="left:502px;top:258px;width:196px;height:36px">Make an Appointment</div>
  <div class="abs dots"><span></span><span></span><span></span><span></span></div>
  <form class="abs search">
    <div class="field select" style="left:210px;width:206px">Type For Counselling</div>
    <div class="field select" style="left:438px;width:122px">City</div>
    <div class="field select" style="left:570px;width:170px">Enter Your Suburb</div>
    <div class="field" style="left:752px;width:164px">Search in radius (in km)</div>
    <div class="field select" style="left:918px;width:38px;padding:11px 6px">10</div>
    <div class="search-go"><svg width="14" height="14" viewBox="0 0 14 14"><circle cx="6" cy="6" r="4.5" fill="none" stroke="#fff" stroke-width="2"/><path d="M9.5 9.5 L13 13" stroke="#fff" stroke-width="2"/></svg></div>
  </form>
</section>

<section class="provide">
  <h2 class="section-title" style="top:680px">WHAT WE PROVIDE ?</h2>
  <div class="provide-col" style="left:217px;top:776px">
    <div class="provide-icon" style="background:var(--teal)" role="img" aria-label="Anxiety icon"></div>
    <div class="provide-label">Anxiety</div><div class="provide-rule" style="background:var(--teal)"></div>
    <div class="provide-card">Do you feel tense, edgy and wound up? Do you worry a lot, or think in obsessive ways? Do you avoid situations that make you anxious? Do you sometimes have panic attacks? Are you still affected by a past trauma? We can help.</div>
  </div>
  <div class="provide-col" style="left:490px;top:776px">
    <div class="provide-icon" style="background:var(--blue)" role="img" aria-label="Depression icon"></div>
    <div class="provide-label">Depression</div><div class="provide-rule" style="background:var(--blue)"></div>
    <div class="provide-card">Are you feeling empty, hopeless and despairing? Do you have huge ups and downs? Or do you have filter depression (discomfort with yourself, antagonistic, exaggerated behaviour &amp; avoidance) or post baby blues?</div>
  </div>
  <div class="provide-col" style="left:762px;top:776px">
    <div class="provide-icon" style="background:var(--purple)" role="img" aria-label="Stress icon"></div>
    <div class="provide-label">Stress</div><div class="provide-rule" style="background:var(--purple)"></div>
    <div class="provide-card">Do you feel tired but also wired up? Do you struggle with too many expectations? Are you exhausted and close to burnout? Do you have trouble sleeping and/or relaxing? Is there no fun in your life? We can help you.</div>
  </div>
  <div class="btn teal" style="left:230px;top:1083px;width:194px;height:34px;text-transform:none">Take our Depression Quiz now</div>
  <div class="btn blue" style="left:503px;top:1083px;width:194px;height:34px;text-transform:none">Take our Anxiety Quiz now</div>
  <div class="btn purple" style="left:796px;top:1083px;width:152px;height:34px;text-transform:none">Take our Stress Quiz now</div>
</section>

<section class="abs match" role="img" aria-label="Photo of a client talking with a psychologist, blue tint">
  <h2>GREAT MATCH GUARANTEE</h2>
  <p class="sub">We know how important it is to find the right psychologist to help.</p>
  <p class="point" style="left:218px;width:400px">Call our Client Care Consultants to be personally matched with one of our psychologists.</p>
  <p class="point" style="left:628px;width:440px">After your first session, if you don't feel the psychologist is the right fit, we will re-match you and provide a complimentary next session.</p>
  <div class="btn purple" style="left:502px;top:380px;width:196px;height:36px">Find Your Match Now</div>
</section>

<section class="blog">
  <h2 class="section-title" style="top:1844px">BLOG POSTS</h2>
  <article class="abs blog-card">
    <div class="blog-img" role="img" aria-label="Photo of a worried woman at a window">
      <span class="ic" style="left:132px"></span><span class="ic" style="left:170px"></span>
    </div>
    <h3>Do you have Agoraphobia?</h3>
    <p>Do you struggle to leave the house without a friend? Are you frightened of what might happen if you get stuck on a busy train or in an elevator on your own? Do you feel a sense of panic at the thought of being left alone or in a large crowd of people? Do you do everything in your power to avoid these situations? If so, it is possible you may be suffering from Agoraphobia.</p>
    <div class="btn teal" style="left:345px;top:202px;width:86px;height:32px;text-transform:none">Read More</div>
    <div class="share">Share <svg width="14" height="10" viewBox="0 0 14 10"><rect x=".5" y=".5" width="13" height="9" fill="none" stroke="#888"/><path d="M.5 .5 L7 5.5 L13.5 .5" fill="none" stroke="#888"/></svg></div>
  </article>
</section>

<section class="abs faq">
  <h2 class="section-title" style="top:52px">FAQ's</h2>
  <div class="abs faq-bar">Exciting news in Treating Anxiety and Depression<span class="box"></span></div>
  <div class="faq-item" style="top:184px">Why come to us for help with your Anxiety and Depression?</div>
  <div class="faq-item" style="top:240px">Costs of counselling sessions?</div>
  <div class="faq-item" style="top:296px">What rebates are available?</div>
  <div class="faq-item" style="top:352px">What factor creates the best therapeutic help for you?</div>
  <div class="faq-item" style="top:408px">What to Expect on Your First Appointment</div>
  <div class="abs faq-text">
    <p>In recent years there has been a huge amount of research in neuroscience with exciting new discoveries into what is happening in the brain when you are experiencing depression and anxiety and why you are suffering in these ways. This enables us to create wonderful new methodologies for helping you overcome these problems. The newer methodologies of Mindfulness and Compassionate Therapy are showing extremely positive results.</p>
    <p style="margin-top:22px">So you do not have to continue to suffer. We now have very powerful and proven methods for helping you overcome anxiety, stress and depression that don't have you relying solely on medication.</p>
  </div>
</section>

<section class="ready">
  <h2 class="section-title" style="top:2898px">READY TO GET STARTED?</h2>
  <p class="abs ready-text">Every day across Australia, millions of people struggle with depression, anxiety and stress. We're passionate about changing that.</p>
  <div class="btn teal" style="left:502px;top:3006px;width:196px;height:36px">Request an Appointment</div>
</section>

<section class="abs locations">
  <div class="map" role="img" aria-label="Map of Australia showing the states, with Queensland highlighted for Brisbane"></div>
</section>
<h3 class="abs loc-title">BRISBANE</h3>
<ul class="abs loc-list"><li>Brisbane CBD</li><li>Carindale</li><li>Ashgrove</li><li>Indooroopilly</li><li>Parkinson</li><li>Springfield</li></ul>

<footer class="abs footer">
  <div class="logo"><i></i>Calmbridge</div>
  <div class="phone"><svg width="14" height="14" viewBox="0 0 14 14"><path d="M3 1 L5 1 L6 4 L4.5 5.5 Q6 8.5 8.5 9.5 L10 8 L13 9 L13 11 Q13 13 11 13 Q1 12 1 3 Q1 1 3 1 Z" fill="#999"/></svg>1300 555 019</div>
  <ul class="foot-col" style="left:384px"><li>Home</li><li>Counselling Types</li><li>Psychologist Locations</li><li>FAQs</li><li>Fees &amp; Rebates</li><li>Quizzes</li><li>Contact</li></ul>
  <ul class="foot-col" style="left:588px"><li>About Us</li><li>Therapies We Use</li><li>Join Our Associate Program</li><li>Blog</li></ul>
  <div class="join">
    <h4>Are You A Psychologist?</h4>
    <p>If you're interested in joining our Associate Psychologist team, click here for more details. Currently united Psychologist Associate?</p>
    <div class="btn teal" style="left:14px;top:112px;width:170px;height:28px">Click Here to Join Us</div>
  </div>
</footer>
<div class="abs copyright">© 2016 Company Name &nbsp;|&nbsp; All Rights Reserved</div>

</body>
</html>
```